Invite Card (Ministers) (business cards used for personal invitation to our church)

I need a business card sized advertisement. The card is a replacement for the attached card only much much cooler. I do not want a image background but more of a vectored, flat look with advertising colors.

I have attached a new image of the couple to replace the old image and a new logo to replace the old logo.

I need a PSD with ALL of the layers un-merged & unlocked

The back of the card should carry the same information as the old card.

Use advertising color and a modern flat look and feel.

Target Market(s)

professional audience

Industry/Entity Type

Non-Profit

Contact Information for Business Card

The card is a replacement for the attached card only much much cooler. I do not want a image background but more of a vectored, flat look with advertising colors.

Font styles to use
Sans Serif

Requirements
Must have
• Must have new logo, new image of couple
Should not have
• graphical background

```html
<!DOCTYPE html>
<html lang="en">
<head>
<meta charset="utf-8">
<title>Invite Card – Front and Back</title>
<link rel="stylesheet" href="https://fonts.googleapis.com/css2?family=Noto+Sans:wght@400;700;800&family=Dancing+Script:wght@500&display=swap">
<style>
  :root {
    --page: #f3ece0;
    --sky-top: #43a9c3;
    --sky-mid: #62c4da;
    --sky-low: #a9dde9;
    --sky-foot: #eef8fb;
    --maroon: #8e1b1f;
    --white: #ffffff;
    --photo-a: #3a3f4e;
    --photo-b: #b77fb8;
  }
  * { margin: 0; padding: 0; box-sizing: border-box; }
  html, body { width: 1189px; height: 1200px; overflow: hidden; background: var(--page); }
  .canvas { position: relative; width: 1189px; height: 1200px; }

  .card {
    position: absolute;
    left: 171px;
    width: 856px;
    height: 487px;
    overflow: hidden;
    background: linear-gradient(180deg, var(--sky-top) 0%, var(--sky-mid) 30%, var(--sky-low) 70%, var(--sky-foot) 100%);
    box-shadow: 0 6px 14px rgba(0,0,0,0.18);
    font-family: "Noto Sans", Arial, sans-serif;
    color: var(--maroon);
  }
  .card--front { top: 69px; }
  .card--back { top: 628px; }

  .waves { position: absolute; inset: 0; width: 100%; height: 100%; }

  .couple-photo {
    position: absolute;
    left: 0; top: 131px;
    width: 441px; height: 356px;
    background: linear-gradient(90deg, var(--photo-a) 0%, var(--photo-a) 55%, var(--photo-b) 60%, var(--photo-b) 100%);
    border-radius: 120px 140px 0 0;
  }

  .brand-name {
    position: absolute;
    left: 494px; top: 40px;
    width: 300px;
    text-align: center;
    font-weight: 800;
    font-size: 200px;
    line-height: 1;
    letter-spacing: -6px;
    color: var(--white);
  }

  .invite {
    position: absolute;
    font-family: "Dancing Script", cursive;
    font-weight: 500;
    font-size: 66px;
    line-height: 1;
    color: var(--maroon);
  }
  .invite--top { left: 494px; top: 300px; }
  .invite--bottom { left: 548px; top: 372px; }

  .contact { position: absolute; left: 0; right: 0; top: 90px; text-align: center; }
  .contact__web { font-size: 36px; font-weight: 400; line-height: 1.2; }
  .contact__address { margin-top: 14px; font-size: 29px; line-height: 1.25; }

  .schedule { position: absolute; left: 121px; width: 616px; top: 272px; list-style: none; font-size: 30px; }
  .schedule__row { display: flex; align-items: baseline; line-height: 1.45; }
  .schedule__leader { flex: 1; border-bottom: 3px dotted var(--maroon); margin: 0 4px 7px; }
</style>
</head>
<body>
<main class="canvas">

  <section class="card card--front" aria-label="Card front">
    <svg class="waves" viewBox="0 0 856 487" aria-hidden="true">
      <path d="M0 95 C160 150 330 220 520 260 C680 290 780 275 856 250 L856 270 C760 300 660 310 520 285 C330 245 170 180 0 125 Z" fill="rgba(255,255,255,0.18)"/>
      <path d="M0 150 C200 170 380 250 600 290 C720 310 800 300 856 290" fill="none" stroke="rgba(255,255,255,0.3)" stroke-width="3"/>
      <circle cx="820" cy="250" r="26" fill="rgba(255,255,255,0.25)"/>
      <circle cx="480" cy="275" r="10" fill="rgba(255,255,255,0.3)"/>
    </svg>
    <div class="couple-photo" role="img" aria-label="Photo of the ministers, a smiling couple in formal clothing"></div>
    <div class="brand-name">GH</div>
    <p class="invite invite--top">You're</p>
    <p class="invite invite--bottom">Invited</p>
  </section>

  <section class="card card--back" aria-label="Card back">
    <svg class="waves" viewBox="0 0 856 487" aria-hidden="true">
      <path d="M0 95 C160 150 330 220 520 260 C680 290 780 275 856 250 L856 270 C760 300 660 310 520 285 C330 245 170 180 0 125 Z" fill="rgba(255,255,255,0.18)"/>
      <path d="M0 150 C200 170 380 250 600 290 C720 310 800 300 856 290" fill="none" stroke="rgba(255,255,255,0.3)" stroke-width="3"/>
      <circle cx="823" cy="226" r="26" fill="rgba(255,255,255,0.25)"/>
      <circle cx="482" cy="250" r="10" fill="rgba(255,255,255,0.3)"/>
      <circle cx="367" cy="439" r="18" fill="rgba(255,255,255,0.25)"/>
    </svg>
    <div class="contact">
      <p class="contact__web">GraceHarbor.org</p>
      <p class="contact__address">2840 W. Cedar Lane - Mesquite, TX 75150<br>1-800-555-0142</p>
    </div>
    <ul class="schedule">
      <li class="schedule__row"><span>Sunday</span><span class="schedule__leader"></span><span>9.00 AM</span></li>
      <li class="schedule__row"><span>Sunday</span><span class="schedule__leader"></span><span>11.00 AM</span></li>
      <li class="schedule__row"><span>Wed.Bible Class</span><span class="schedule__leader"></span><span>7.00 PM</span></li>
    </ul>
  </section>

</main>
</body>
</html>
```